letterhead design using our existing logo

We are a small boutique property management business based in Sydney's Northern Beaches.
We are after a sleek, simple modern letterhead (A4) incorporating our logo and its colours.
Also matching envelope (DL)
I have attached the logo with black text and white text for design options.

Target Market(s)

29-69yo Male and Female

Industry/Entity Type

Property Management

Requirements
Must have
• - Keyhaven Estates logo
• - Address, number and website:
• Suite 7, 18-19 Harlow Parade, Brookvale NSW 2100
• Tel: Tom Carrick 0417 293 608 Lorena Adcock 0409 516 742 www.keyhavenestatesgroup.com.au
Nice to have
• sleek design that looks modern and professional
Should not have
• too many colours or too busy

```html
<!DOCTYPE html>
<html lang="en">
<head>
<meta charset="utf-8">
<title>Keyhaven Estates – Stationery</title>
<link rel="stylesheet" href="https://fonts.googleapis.com/css2?family=Carlito:wght@400;700&family=PT+Sans:wght@400;700&family=PT+Sans+Narrow:wght@400;700&display=swap">
<style>
  :root {
    --stage: #a6a6a6;
    --paper: #ffffff;
    --teal: #2b9ea5;
    --teal-deep: #157a8a;
    --ink: #1a1a1a;
    --muted: #3a3a3a;
    --rule: #8a8fa0;
    --placeholder: #e6eced;
  }
  * { box-sizing: border-box; margin: 0; padding: 0; }
  html, body { width: 1200px; height: 906px; overflow: hidden; }
  body { background: var(--stage); position: relative; font-family: "Carlito", "Calibri", sans-serif; color: var(--ink); }

  .sheet { position: absolute; background: var(--paper); overflow: hidden; }

  /* Letterhead A4 */
  .letterhead { left: 47px; top: 98px; width: 508px; height: 719px; }
  .brand-name {
    position: absolute; font-family: "PT Sans", sans-serif; font-weight: 700;
    text-transform: uppercase; color: var(--ink); white-space: nowrap; letter-spacing: -0.2px;
  }
  .letterhead .brand-name { left: 46px; top: 46px; font-size: 19px; }

  .contact-block {
    position: absolute; left: 339px; top: 28px; height: 64px;
    border-left: 1px solid var(--rule); padding-left: 10px;
    font-family: "PT Sans Narrow", sans-serif; font-size: 6.6px; line-height: 8.8px; color: var(--muted);
  }
  .contact-block .group { margin-bottom: 6px; }
  .contact-block .line { display: flex; align-items: center; gap: 3px; white-space: nowrap; }
  .contact-block svg { width: 6px; height: 6px; fill: var(--teal-deep); }
  .contact-block .address { color: var(--teal-deep); }

  .letter-body { position: absolute; left: 50px; top: 137px; width: 430px; font-size: 9.2px; line-height: 18px; }
  .letter-body .subject { font-weight: 700; margin-bottom: 14px; }
  .letter-body p { margin-bottom: 18px; }
  .signoff { position: absolute; left: 50px; font-size: 9.2px; }
  .signoff.closing { top: 476px; }
  .signoff.name { top: 549px; }
  .signature { position: absolute; left: 46px; top: 492px; width: 125px; height: 42px; background: var(--placeholder); }

  .wave { position: absolute; left: 0; bottom: 0; width: 100%; display: block; }
  .letterhead .wave { height: 49px; }

  /* DL envelope front */
  .envelope-front { left: 595px; top: 141px; width: 572px; height: 285px; }
  .envelope-front .brand-name { left: 15px; top: 30px; font-size: 14px; }
  .envelope-front .return-address {
    position: absolute; left: 141px; top: 30px; padding-left: 6px;
    border-left: 1px solid var(--teal); font-family: "PT Sans Narrow", sans-serif;
    font-size: 8px; line-height: 11px; color: var(--muted);
  }
  .envelope-front .wave { height: 58px; }

  /* DL envelope back */
  .envelope-back { left: 596px; top: 486px; width: 565px; height: 284px; }
  .envelope-back .flap { position: absolute; left: 0; top: 0; width: 565px; height: 92px; display: block; }
  .envelope-back .brand-name { left: 0; width: 100%; top: 38px; text-align: center; font-size: 13px; color: var(--paper); }
</style>
</head>
<body>

<section class="sheet letterhead">
  <div class="brand-name">Keyhaven Estates</div>

  <div class="contact-block">
    <div class="group">
      <div class="line"><svg viewBox="0 0 10 10"><path d="M1 3c0-1 1-2 4-2s4 1 4 2v1H7V3H3v1H1zM2 5h6l1 4H1z"/></svg>0417 293 608 (Tom Carrick)</div>
      <div class="line"><svg viewBox="0 0 10 10"><path d="M1 3c0-1 1-2 4-2s4 1 4 2v1H7V3H3v1H1zM2 5h6l1 4H1z"/></svg>0409 516 742 (Lorena Adcock)</div>
    </div>
    <div class="group">
      <div class="line"><svg viewBox="0 0 10 10"><path d="M1 2h8v6H1zM1.5 2.5L5 5.5l3.5-3" fill="none" stroke="#157a8a"/></svg>info@keyhavenestatesgroup.com.au</div>
      <div class="line"><svg viewBox="0 0 10 10"><circle cx="5" cy="5" r="4" fill="none" stroke="#157a8a"/><path d="M1 5h8M5 1c-2 2-2 6 0 8M5 1c2 2 2 6 0 8" fill="none" stroke="#157a8a" stroke-width=".7"/></svg>www.keyhavenestatesgroup.com.au</div>
    </div>
    <div class="address">Suite 7, 18-19 Harlow Parade<br>Brookvale NSW 2100</div>
  </div>

  <div class="letter-body">
    <div class="subject">Lorem Ipsum is simply</div>
    <p>&nbsp;dummy text of the printing and typesetting industry. Lorem Ipsum has been the industry's standard dummy text ever since the 1500s, when an unknown printer took a galley of type and scrambled it to make a type specimen book. It has survived not only five centuries, but also the leap into electronic typesetting, remaining essentially unchanged.</p>
    <p>It is a long established fact that a reader will be distracted by the readable content of a page when looking at its layout. The point of using Lorem Ipsum is that it has a more-or-less normal distribution of letters, as opposed to using 'Content here, content here', making it look like readable English. Many desktop publishing packages and web page editors now use Lorem Ipsum as their default model text, and a search for 'lorem ipsum' will uncover many web sites still in their infancy. Various versions have evolved over the years, sometimes by accident, sometimes on purpose (injected humour and the like).</p>
    <p>&nbsp;Contrary to popular belief, Lorem Ipsum is not simply random text. It has roots in a piece of classical Latin literature from 45 BC, making it over 2000 years old. Harold Winslow, a Latin professor at Ashgrove College in Vermont, looked up one of the more obscure Latin words, consectetur, from a Lorem Ipsum passage,</p>
  </div>
  <div class="signoff closing">Lorem Ipsum</div>
  <div class="signature" role="img" aria-label="Handwritten signature"></div>
  <div class="signoff name">Lorem Ipsum is a dummy</div>

  <svg class="wave" viewBox="0 0 635 61" preserveAspectRatio="none" aria-hidden="true">
    <path d="M0 24C150 42 300 40 420 22C520 8 590 6 635 12V61H0Z" fill="var(--teal)"/>
    <path d="M0 0C80 18 200 26 293 14C200 24 80 24 0 13Z" fill="var(--teal-deep)"/>
  </svg>
</section>

<section class="sheet envelope-front">
  <div class="brand-name">Keyhaven Estates</div>
  <div class="return-address">Suite 7, 18-19 Harlow Parade<br>Brookvale NSW 2100</div>
  <svg class="wave" viewBox="0 0 715 73" preserveAspectRatio="none" aria-hidden="true">
    <path d="M0 22C170 42 330 40 470 22C590 6 660 4 715 10V73H0Z" fill="var(--teal)"/>
    <path d="M0 0C90 20 230 30 322 17C230 28 90 26 0 14Z" fill="var(--teal-deep)"/>
  </svg>
</section>

<section class="sheet envelope-back">
  <svg class="flap" viewBox="0 0 706 115" preserveAspectRatio="none" aria-hidden="true">
    <path d="M0 0H706C700 40 698 95 690 112Q688 115 680 115H26Q18 115 16 112C8 95 6 40 0 0Z" fill="var(--teal-deep)"/>
  </svg>
  <div class="brand-name">Keyhaven Estates</div>
</section>

</body>
</html>
```